Corvimo Business Card

Corvimo is a young and energetic software development consultancy. We spend our time on the road working with clients on their sites an meeting new potential customers and employees!

We need a sharp, vibrant and memorable business card that will inspires those that receive it to look after it as it oozes quality and is a nice thing in its own right.

We like bold colours and distinctive design. So show us what you can do.

In terms of information on the card, it would be good to see:

* Our logo (Obviously :) )
* Employee name
* Email
* Website address
* Mobile number
* Full company name (Corvimo ltd)
* Registered company number
* Registered company address

Industry/Entity Type

Software

Requirements
Nice to have
• We are thinking that having a QR Code on the business card could be a good way of adding active marketing. It would be good to see if you are able to merge the kind of element in to your designs!

Maybe something special could be achieved using a visual QR Code like those produced at http://www.pixoranta.example/ ? You have our media so feel free to have a play.

```html
<!DOCTYPE html>
<html lang="en">
<head>
<meta charset="utf-8">
<title>Corvimo Business Card</title>
<link rel="stylesheet" href="https://fonts.googleapis.com/css2?family=Questrial&family=Montserrat:wght@600;700&display=swap">
<style>
  :root {
    --page-bg: #e4e4e4;
    --card-white: #f6f6f6;
    --brand-red: #b5232e;
    --text-grey: #8a8a8a;
    --text-dark: #5e5e5e;
    --soft-grey: #d9d9d9;
    --back-text: #f3dede;
  }
  * { margin: 0; padding: 0; box-sizing: border-box; }
  html, body { width: 1200px; height: 919px; overflow: hidden; }
  body {
    background: var(--page-bg);
    font-family: "Questrial", "Century Gothic", sans-serif;
    position: relative;
  }
  .card {
    position: absolute;
    width: 540px;
    height: 310px;
    border-radius: 26px;
    overflow: hidden;
    box-shadow: 0 6px 18px rgba(0,0,0,0.12);
  }
  .card-front { left: 40px; top: 304px; background: var(--card-white); }
  .card-back { left: 620px; top: 304px; background: var(--brand-red); }

  .wordmark {
    position: absolute;
    font-family: "Questrial", sans-serif;
    font-size: 38px;
    letter-spacing: 2px;
    line-height: 1;
  }
  .card-front .wordmark { left: 36px; top: 108px; color: var(--brand-red); }
  .card-back .wordmark { left: 230px; top: 118px; color: #ffffff; }

  .front-decor {
    position: absolute; right: -40px; top: -30px;
    width: 190px; height: 190px; border-radius: 50%;
    background: var(--soft-grey); opacity: 0.55;
  }
  .back-decor {
    position: absolute; left: 40px; top: 170px;
    width: 170px; height: 170px; border-radius: 50%;
    background: rgba(255,255,255,0.08);
  }

  .person { position: absolute; left: 300px; top: 34px; }
  .person-name {
    font-family: "Montserrat", sans-serif; font-weight: 700;
    font-size: 15px; color: var(--text-dark); letter-spacing: 0.5px;
  }
  .person-role { font-size: 10px; color: var(--text-grey); letter-spacing: 1.5px; margin-top: 1px; }

  .contact-list { position: absolute; font-size: 12px; color: var(--text-grey); line-height: 1.5; }
  .contact-list .label {
    font-family: "Montserrat", sans-serif; font-weight: 600;
    color: var(--brand-red); margin-right: 4px;
  }
  .contact-phones { left: 360px; top: 150px; }
  .contact-online { left: 180px; top: 206px; }

  .address {
    position: absolute; left: 36px; top: 244px;
    font-size: 12px; color: var(--text-grey); line-height: 1.5;
  }

  .registration {
    position: absolute; left: 230px; top: 176px;
    font-size: 12px; color: var(--back-text); line-height: 1.6;
  }
</style>
</head>
<body>
  <section class="card card-front" aria-label="Business card front">
    <div class="front-decor"></div>
    <div class="wordmark">CORVIMO</div>
    <div class="person">
      <div class="person-name">JAMIE ROWE</div>
      <div class="person-role">MANAGER</div>
    </div>
    <div class="contact-list contact-phones">
      <div><span class="label">Mobile:</span>+61 2 5550 1482</div>
      <div><span class="label">Phone:</span>+61 2 5550 1490</div>
    </div>
    <div class="contact-list contact-online">
      <div><span class="label">Email:</span>info@corvimo.com</div>
      <div><span class="label">Web:</span>www.corvimo.com</div>
    </div>
    <address class="address" style="font-style: normal;">
      14 Wrenfield Road<br>
      Harlow Essex, CM174QT
    </address>
  </section>

  <section class="card card-back" aria-label="Business card back">
    <div class="back-decor"></div>
    <div class="wordmark">CORVIMO</div>
    <p class="registration">
      Corvimo Ltd is registered in England<br>
      and Wales. Reg. No: 7291564
    </p>
  </section>
</body>
</html>
```